Northcliff Thermal Services Ltd Needs a 2 sided A5 Flyer Design

We need a flyer design for our company to promote Air and ground Source Heat Pumps in the Devon and Cornwall region of the UK.

Our Government has launched the DWB (domestic warmth bonus) a 7 year quarterly payment to offset the cost of installation..
Homeowners currently using OIL or LPG gas for there heating and hot water will save up to 50% on there energy bill by swapping to a heat pump,
Currently education is needed to the potential end user on the benefits of heat pumps,
This flyer will be part of an initial start point to get the homeowner to book a free survey to discuss there options, We are a renewable energy company with great local knowledge, and a wealth of experience ......

KEY points SAVINGS OF UP TO 50% on OIL or LPG heating and hot water systems

DWB PAYMENTS FROM GOVERNMENT FOR 7 years

HONEST IMPARTIAL ADVICE ON SOLUTIONS

FREE SURVEYS ON ALL RENEWABLE SOLUTIONS AND COSTINGS. website www.ncthermal.co.uk have included some potential wording

LOGOS FROM SUPPLIERS

We think side one should be high impact on high oil and LPG gas costs, harm to environment and potential 50% savings with a heat pump. Side 2 to be DWB 7 year quarterly payment and a little about our company offering expertise and free impartial advice and survey

general theme a "striking call to action"

Target Market(s)

Target market is 40 to 60 year old home owners that are off gas grid and use oil or LPG for heating and hot water

Industry/Entity Type

Environment

Font styles to use
Serif
Sans Serif

Colors
33a6d7
f04a50
00a88f
fbed22

Requirements
Must have
• savings 50% on oil or LPG energy costs for heating and hot water

DWB (domestic warmth bonus) government backed payments to offset cost of instalation

7 year payments averaging £1000 a year

FREE impartial advice and surveys

```html
<!DOCTYPE html>
<html lang="en">
<head>
<meta charset="utf-8">
<title>Northcliff Thermal Services Ltd – Heat Pump Flyer</title>
<link rel="stylesheet" href="https://fonts.googleapis.com/css2?family=Raleway:wght@200;300;400&family=Roboto+Condensed:wght@700&family=Montserrat:wght@700&display=swap">
<style>
  :root {
    --page-bg: #efefef;
    --paper: #ffffff;
    --lime: #b9d531;
    --lime-deep: #8dc63f;
    --sky: #5d8fd8;
    --sky-soft: #c9dcf3;
    --brand-red: #f04a50;
    --brand-blue: #33a6d7;
    --brand-green: #00a88f;
    --text-grey: #7b7b7b;
    --text-dark: #3d3d3d;
    --tank: #2e3432;
    --bottle: #ef4f36;
    --logo-green: #6dab2f;
  }
  * { box-sizing: border-box; margin: 0; padding: 0; }
  html, body { width: 1200px; height: 1000px; overflow: hidden; }
  body { background: var(--page-bg); position: relative; font-family: "Raleway", sans-serif; }

  .flyer-side { position: absolute; top: 127px; width: 537px; height: 755px; background: var(--paper); overflow: hidden; }
  .side-front { left: 67px; }
  .side-back { left: 627px; }

  /* ---------- front side ---------- */
  .front-sky { position: absolute; left: 198px; top: 0; width: 339px; height: 230px;
    background: linear-gradient(200deg, var(--sky) 0%, var(--sky-soft) 45%, rgba(255,255,255,0) 85%); }
  .benefits-panel { position: absolute; left: 0; top: 0; width: 198px; height: 421px; background: var(--lime);
    border-bottom-right-radius: 34px; padding: 24px 14px 0 22px; }
  .benefits-text { font-family: "Roboto Condensed", sans-serif; font-weight: 700; color: #fff; font-size: 11.4px; line-height: 15.4px; }
  .heatpump-photo { position: absolute; left: 166px; top: -28px; width: 228px; height: 228px; border-radius: 50%;
    border: 6px solid #fff; background: linear-gradient(135deg, #d9dcdf, #f4f4f2 55%, #9fb3c8); }
  .headline { position: absolute; left: 238px; top: 222px; font-weight: 200; color: var(--text-grey);
    font-size: 31px; line-height: 38px; letter-spacing: -0.5px; white-space: nowrap; }
  .save-word { position: absolute; left: 236px; top: 342px; font-weight: 200; font-size: 66px; line-height: 66px;
    letter-spacing: -1px; color: #c6d82e; white-space: nowrap; }
  .compared { position: absolute; left: 238px; top: 418px; font-weight: 300; color: var(--text-grey); font-size: 28px; line-height: 28px; white-space: nowrap; }
  .compared-small { position: absolute; left: 242px; top: 477px; font-weight: 300; color: #9a9a9a; font-size: 12px; white-space: nowrap; }
  .saving-diamond { position: absolute; left: 372px; top: 340px; width: 150px; height: 150px; }
  .oil-tank-photo { position: absolute; left: 0; top: 438px; width: 236px; height: 210px;
    background: linear-gradient(180deg, #3b4240, var(--tank)); border-radius: 60px 40px 0 0; }
  .bottles-photo { position: absolute; left: 238px; top: 498px; width: 299px; height: 148px;
    background: linear-gradient(90deg, var(--bottle), #f26a4c 50%, var(--bottle)); border-radius: 40px 40px 8px 8px; }
  .footnote-band { position: absolute; left: 0; top: 648px; width: 311px; height: 107px;
    background: linear-gradient(90deg, #5aa3d4, #b0708a 55%, var(--brand-red)); padding: 44px 10px 0 22px; color: #fff; }
  .footnote-band p { font-family: "Roboto Condensed", sans-serif; font-size: 9.6px; line-height: 12px; white-space: nowrap; }
  .footnote-band .note { font-weight: 400; font-family: "Raleway", sans-serif; }
  .footnote-band .strong { font-weight: 700; }

  .brand-lockup { position: absolute; display: flex; align-items: center; gap: 8px; }
  .brand-mark { width: 16px; height: 16px; border-radius: 50%; background: var(--logo-green); flex: none; }
  .brand-name { font-family: "Raleway", sans-serif; font-weight: 400; color: var(--text-dark); line-height: 1.15; white-space: nowrap; }
  .brand-name span { display: block; }
  .front-brand { left: 338px; top: 688px; }
  .front-brand .brand-name { font-size: 20px; }
  .front-brand .brand-name span + span { font-size: 12px; }

  /* ---------- back side ---------- */
  .back-sky { position: absolute; left: 0; top: 0; width: 238px; height: 330px;
    background: linear-gradient(170deg, var(--sky) 0%, var(--sky-soft) 35%, rgba(255,255,255,0) 80%); }
  .scheme-intro { position: absolute; left: 28px; top: 50px; width: 186px; font-weight: 300; color: var(--text-grey);
    font-size: 17.5px; line-height: 25.2px; }
  .scheme-intro strong { font-family: "Montserrat", sans-serif; font-weight: 700; color: var(--text-dark); font-size: 17.5px; line-height: 24px; }
  .company-panel { position: absolute; left: 238px; top: 0; width: 299px; height: 421px;
    background: linear-gradient(160deg, var(--lime) 0%, var(--lime-deep) 100%); border-bottom-left-radius: 34px;
    padding: 52px 22px 0 32px; }
  .company-panel p { font-family: "Roboto Condensed", sans-serif; font-weight: 700; color: #fff; font-size: 11px;
    line-height: 17.2px; text-align: justify; margin-bottom: 17px; }
  .unit-photo { position: absolute; left: 23px; top: 393px; width: 246px; height: 262px; border-radius: 40px;
    background: linear-gradient(135deg, #a14f3c 0%, #e8e8e6 30%, #f5f5f4 60%, #86a35a 100%); }
  .contact-note { position: absolute; left: 283px; top: 476px; width: 230px; text-align: center; font-weight: 300;
    color: #8a8a8a; font-size: 8.4px; line-height: 10.6px; }
  .back-brand { left: 300px; top: 535px; }
  .back-brand .brand-name { font-size: 21px; }
  .back-brand .brand-name span + span { font-size: 12px; }
  .website { position: absolute; left: 313px; top: 628px; font-weight: 400; color: var(--text-grey); font-size: 17px; white-space: nowrap; }
  .supplier-row { position: absolute; left: 22px; top: 680px; width: 495px; display: flex; justify-content: space-between; align-items: center; }
  .supplier-badge { height: 30px; border-radius: 6px; }
  .badge-scheme { width: 56px; background: #f6a54a; }
  .badge-a { width: 92px; background: #2fa2d9; border-radius: 15px; }
  .badge-b { width: 68px; background: #d81e2a; }
  .badge-c { width: 96px; background: #1e2f6b; border-radius: 15px; }
  .badge-d { width: 56px; height: 40px; background: #e9eef3; border: 1px solid #c5ccd4; border-radius: 3px; }
  .address { position: absolute; left: 0; width: 537px; top: 723px; text-align: center; font-weight: 400; color: var(--text-grey); font-size: 12.4px; white-space: nowrap; }
</style>
</head>
<body>

<section class="flyer-side side-front">
  <div class="front-sky"></div>
  <div class="heatpump-photo" role="img" aria-label="Photo of an outdoor air source heat pump unit against a brick wall"></div>
  <div class="benefits-panel">
    <p class="benefits-text">Air source heat pumps will fit into your current radiator heating system in most cases, and will provide all of your heating and hot water needs for the home. You will no longer have to pay for high priced Oil and LPG. DWB payments are paid by the Government for 7 years every quarter directly into your bank to offset the initial cost of equipment. Ongoing savings year on year of 50% compared to your current fuel usage. Saving between £500 and £1200. Heat pumps require little maintenance and have a life expectancy of 25+ years; where after just the main unit would have to be replaced, making replecement expectation similar to a standard boiler.</p>
  </div>

  <h1 class="headline">BUY AN AIR AND<br>GROUND SOURCE<br>HEAT PUMP AND</h1>
  <div class="save-word">SAVE</div>
  <svg class="saving-diamond" viewBox="0 0 150 150" aria-label="50%">
    <defs>
      <linearGradient id="diamondFill" x1="0" y1="0" x2="1" y2="1">
        <stop offset="0" stop-color="#d4e02a"/>
        <stop offset="0.5" stop-color="#f2a23a"/>
        <stop offset="1" stop-color="#f04a50"/>
      </linearGradient>
    </defs>
    <rect x="23" y="23" width="104" height="104" rx="8" transform="rotate(45 75 75)" fill="url(#diamondFill)"/>
    <text x="72" y="92" text-anchor="middle" font-family="Raleway, sans-serif" font-weight="200" font-size="50" fill="#fff">50<tspan font-size="26" dy="-4">%</tspan></text>
  </svg>
  <div class="compared">compared<br>to these</div>
  <div class="compared-small">hot water systems</div>

  <div class="bottles-photo" role="img" aria-label="Photo of four red LPG gas bottles"></div>
  <div class="footnote-band">
    <p class="note">*Compared to oil or LPG for heat and hot water</p>
    <p class="strong">Government backed dwb domestic warmth bonus</p>
    <p class="strong">£1,000 A year payments on average for 7 years for instalation</p>
  </div>
  <div class="oil-tank-photo" role="img" aria-label="Photo of a dark green plastic domestic oil tank"></div>

  <div class="brand-lockup front-brand">
    <span class="brand-mark"></span>
    <p class="brand-name"><span>Northcliff</span><span>Thermal Services Ltd</span></p>
  </div>
</section>

<section class="flyer-side side-back">
  <div class="back-sky"></div>
  <p class="scheme-intro">In October of 2014 the Government finalised the groundbreaking <strong>DWB domestic warmth bonus</strong>. We are the first country in the world to give payments to cover the installation costs of renewable technology based around heating and hot water.</p>

  <div class="company-panel">
    <p>At Northcliff Thermal Services we are in a unique position to advise you on the options open to you to replace your Oil and LPG boilers in favour of products that are 50% cheaper to run and are also kinder to the environment.</p>
    <p>We have 15 years experience in the Renewable Energy market and are not tied to one supplier or one technology. This puts us in a position to discuss ALL the options that are open to you to enable you to make a correct informed decision.</p>
    <p>We are able to manage your project from start to finish and ongoing servicing; with a staff of 20 we do not sub our work to other contractors allowing us to give the end user confidence and peace of mind before, during and after install.</p>
    <p>Please get in touch and we are happy to give free impartial advice on options open to you.</p>
  </div>

  <div class="unit-photo" role="img" aria-label="Photo of an air source heat pump unit mounted beside a brick house"></div>
  <p class="contact-note">Call our Newton Vale based office and ask to speak to Daniel our Energy Consultant or Owen Hartley our Technical Director and they will be pleased to inform you further</p>

  <div class="brand-lockup back-brand">
    <span class="brand-mark"></span>
    <p class="brand-name"><span>Northcliff</span><span>Thermal Services Ltd</span></p>
  </div>
  <p class="website">www.ncthermal.co.uk</p>

  <div class="supplier-row">
    <span class="supplier-badge badge-scheme" role="img" aria-label="DWB scheme badge"></span>
    <span class="supplier-badge badge-a" role="img" aria-label="Thermora supplier badge"></span>
    <span class="supplier-badge badge-b" role="img" aria-label="Valtrix supplier badge"></span>
    <span class="supplier-badge badge-c" role="img" aria-label="Caldera supplier badge"></span>
    <span class="supplier-badge badge-d" role="img" aria-label="Approved installer certification badge"></span>
  </div>
  <p class="address">Unit 7 Harbour Trade Park, Quay Road, Newton Vale, Devon TQ9 2XY T: 01632 960418</p>
</section>

</body>
</html>
```